Business cards and stationary
Venoki Imaging, llc
Professional
Miriam Colfax. Dana Pruitt
Owners
17 Harrow Lane
Bloomingburg, ny 12721 (Miriam )
52 Willowby Road
New Windsor, NY 12553 ( Dana )
Miriam 914-555-0142. /. Dana 845-555-0197
Juniper41@mailvex.com

```html
<!DOCTYPE html>
<html lang="en">
<head>
<meta charset="utf-8">
<title>Venoki Imaging, llc — Business Cards</title>
<link href="https://fonts.googleapis.com/css2?family=Cinzel:wght@400;600&family=Cormorant+Garamond:wght@500;600&display=swap" rel="stylesheet">
<style>
  :root {
    --backdrop: #d9d9db;
    --card: #ffffff;
    --brand-blue: #2a5ea8;
    --brand-purple: #8b1f7e;
    --band-blue: #1f74bb;
    --band-purple: #8d2383;
    --ink: #3a3a48;
    --shadow: rgba(0, 0, 0, 0.18);
  }
  * { box-sizing: border-box; margin: 0; padding: 0; }
  html, body {
    width: 1200px;
    height: 895px;
    overflow: hidden;
    background: var(--backdrop);
  }
  .sheet {
    width: 1200px;
    height: 895px;
    display: flex;
    flex-direction: column;
    align-items: center;
    justify-content: center;
    gap: 35px;
  }
  .card {
    position: relative;
    width: 700px;
    height: 400px;
    background: var(--card);
    box-shadow: 0 6px 18px var(--shadow);
    overflow: hidden;
  }

  /* Front face */
  .card-front .sweep {
    position: absolute;
    inset: 0;
    width: 100%;
    height: 100%;
  }
  .brand {
    position: absolute;
    left: 48px;
    top: 58px;
  }
  .brand-name {
    display: flex;
    align-items: center;
    gap: 12px;
    font-family: "Cinzel", serif;
    font-weight: 600;
    font-size: 30px;
    color: var(--brand-blue);
    letter-spacing: 0.5px;
    white-space: nowrap;
  }
  .brand-dot {
    width: 14px;
    height: 14px;
    border-radius: 50%;
    background: var(--brand-blue);
    flex: none;
  }
  .brand-tagline {
    margin-top: 4px;
    margin-left: 26px;
    font-family: "Cormorant Garamond", serif;
    font-weight: 600;
    font-size: 15px;
    letter-spacing: 4px;
    text-transform: uppercase;
    color: var(--brand-purple);
  }
  .contact-list {
    position: absolute;
    left: 48px;
    top: 172px;
    list-style: none;
    display: flex;
    flex-direction: column;
    gap: 9px;
  }
  .contact-item {
    display: flex;
    align-items: center;
    gap: 10px;
    font-family: "Cormorant Garamond", serif;
    font-weight: 600;
    font-size: 17px;
    color: var(--ink);
  }
  .contact-icon {
    width: 18px;
    height: 18px;
    flex: none;
  }
  .owners {
    position: absolute;
    right: 34px;
    bottom: 24px;
    font-family: "Cormorant Garamond", serif;
    font-weight: 600;
    font-size: 19px;
    font-variant: small-caps;
    letter-spacing: 1px;
    color: var(--brand-blue);
    white-space: nowrap;
  }

  /* Back face */
  .card-back {
    display: flex;
    flex-direction: column;
    align-items: center;
    justify-content: center;
    gap: 40px;
  }
  .card-back .brand-name {
    font-size: 38px;
  }
  .web-address {
    font-family: "Cormorant Garamond", serif;
    font-weight: 600;
    font-size: 19px;
    letter-spacing: 2px;
    font-variant: small-caps;
    color: var(--ink);
  }
</style>
</head>
<body>
<main class="sheet">

  <section class="card card-front" aria-label="Business card front">
    <svg class="sweep" viewBox="0 0 700 400" preserveAspectRatio="none" aria-hidden="true">
      <path d="M380,0 C580,30 685,150 700,300 L700,0 Z" fill="var(--band-purple)"/>
      <path d="M440,0 C605,38 690,140 700,238 L700,0 Z" fill="#ffffff"/>
      <path d="M456,0 C615,42 692,138 700,222 L700,0 Z" fill="var(--band-blue)"/>
    </svg>

    <div class="brand">
      <div class="brand-name"><span class="brand-dot"></span>Venoki Imaging, llc</div>
      <div class="brand-tagline">Mobile Ultrasound</div>
    </div>

    <ul class="contact-list">
      <li class="contact-item">
        <svg class="contact-icon" viewBox="0 0 18 18" aria-hidden="true"><circle cx="9" cy="9" r="9" fill="var(--brand-blue)"/><path d="M6 4.5 L7.6 4.5 L8.3 7 L7.2 7.8 C7.8 9.2 8.8 10.2 10.2 10.8 L11 9.7 L13.5 10.4 L13.5 12 C13.5 12.8 12.8 13.5 12 13.5 C8.4 13.3 4.7 9.6 4.5 6 C4.5 5.2 5.2 4.5 6 4.5 Z" fill="#fff"/></svg>
        Miriam 914-555-0142
      </li>
      <li class="contact-item">
        <svg class="contact-icon" viewBox="0 0 18 18" aria-hidden="true"><circle cx="9" cy="9" r="9" fill="var(--brand-blue)"/><path d="M6 4.5 L7.6 4.5 L8.3 7 L7.2 7.8 C7.8 9.2 8.8 10.2 10.2 10.8 L11 9.7 L13.5 10.4 L13.5 12 C13.5 12.8 12.8 13.5 12 13.5 C8.4 13.3 4.7 9.6 4.5 6 C4.5 5.2 5.2 4.5 6 4.5 Z" fill="#fff"/></svg>
        Dana 845-555-0197
      </li>
      <li class="contact-item">
        <svg class="contact-icon" viewBox="0 0 18 18" aria-hidden="true"><circle cx="9" cy="9" r="9" fill="var(--brand-blue)"/><rect x="4.5" y="6" width="9" height="6.5" fill="none" stroke="#fff" stroke-width="1.2"/><path d="M4.5 6 L9 9.6 L13.5 6" fill="none" stroke="#fff" stroke-width="1.2"/></svg>
        Juniper41@mailvex.com
      </li>
      <li class="contact-item">
        <svg class="contact-icon" viewBox="0 0 18 18" aria-hidden="true"><circle cx="9" cy="9" r="9" fill="var(--brand-blue)"/><circle cx="9" cy="9" r="4.6" fill="none" stroke="#fff" stroke-width="1.1"/><path d="M4.4 9 H13.6 M9 4.4 C7 6.5 7 11.5 9 13.6 M9 4.4 C11 6.5 11 11.5 9 13.6" fill="none" stroke="#fff" stroke-width="1"/></svg>
        www.VenokiScan.com
      </li>
    </ul>

    <p class="owners">Miriam Colfax, Dana Pruitt</p>
  </section>

  <section class="card card-back" aria-label="Business card back">
    <div class="brand-name"><span class="brand-dot"></span>Venoki Imaging, llc</div>
    <p class="web-address">www.VenokiScan.com</p>
  </section>

</main>
</body>
</html>
```